A UK based Lettings and Property Management Company - Maple Crest Property

Maple Crest Property rents and manages properties on behalf of owners in Liverpool, UK. We are looking for a clean, fresh modern design which incororates our logo.

In terms of pages we initially require:

Home
Lettings
Property Management
Landlords
Tenants
About
Contact

In would like to use colours compatible with the logo

Target Market(s)

People looking to rent property
Owners looking to use our services to let their property

Industry/Entity Type

Property

Contact Information for Business Card

Logo prominent on one side
Address to be edited by us as we are moving premises in October
Name Gavin Holloway
Tel number 0151 486 2037
e-mail gavin@maplecrestproperty.co.uk

Font styles to use
Sans Serif

Colors

Designer to choose colors to be used in the design.

Requirements
Must have
• Clean lines
• Fresh
• Easy navigation
• Easy editing
• Data capture

```html
<!DOCTYPE html>
<html lang="en">
<head>
<meta charset="utf-8">
<title>Maple Crest Property – Lettings &amp; Property Management</title>
<link rel="stylesheet" href="https://fonts.googleapis.com/css2?family=Open+Sans:wght@400;600;700;800&display=swap">
<style>
:root{
  --navy:#1c2740;
  --blue:#1e9be9;
  --yellow:#f6b21b;
  --orange:#f39c12;
  --red:#e5403a;
  --ink:#2b3245;
  --muted:#8a91a0;
  --line:#e3e6ec;
  --field:#f6f7f9;
  --white:#ffffff;
}
*{box-sizing:border-box;margin:0;padding:0}
html,body{width:758px;height:1200px;overflow:hidden}
body{font-family:"Open Sans",Arial,sans-serif;color:var(--ink);background:var(--white);position:relative}

.hero{position:absolute;left:0;top:0;width:758px;height:340px;
  background:linear-gradient(180deg,#1a2433 0%,#2b3a4d 40%,#4a5a66 70%,#26313f 100%)}
.hero-glow{position:absolute;left:180px;top:120px;width:400px;height:170px;
  background:radial-gradient(ellipse at center,rgba(255,214,150,.28),rgba(0,0,0,0) 70%)}

.site-header{position:absolute;left:0;top:0;width:758px;height:52px;display:flex;align-items:center;padding:0 8px}
.brand{display:flex;align-items:center;gap:6px;background:var(--white);height:40px;padding:0 10px 0 8px}
.brand-mark{width:18px;height:18px;background:var(--navy)}
.brand-name{font-size:13px;font-weight:800;color:var(--navy);text-transform:uppercase;line-height:1;white-space:nowrap}
.main-nav{display:flex;gap:12px;margin-left:auto;margin-right:14px}
.main-nav a{color:var(--white);font-size:7.5px;font-weight:600;text-decoration:none;letter-spacing:.4px;white-space:nowrap}
.btn-submit{background:var(--blue);color:var(--white);font-size:8px;font-weight:700;padding:8px 12px;margin-right:14px;letter-spacing:.5px;white-space:nowrap}

.hero-title{position:absolute;top:160px;width:758px;text-align:center;color:var(--white);font-size:19px;font-weight:700;letter-spacing:.5px}
.hero-title span{color:var(--yellow)}
.hero-sub{position:absolute;top:190px;width:758px;text-align:center;color:#d7dbe2;font-size:9px}

.search-tabs{position:absolute;left:76px;top:243px;display:flex}
.search-tabs span{height:20px;padding:0 10px;font-size:8px;font-weight:700;display:flex;align-items:center;justify-content:center;color:var(--white)}
.tab-rent{background:var(--yellow)}
.tab-manage{background:#9aa1ab}

.search-panel{position:absolute;left:76px;top:263px;width:607px;height:99px;background:var(--white);box-shadow:0 4px 14px rgba(0,0,0,.12)}
.search-fields{position:absolute;left:10px;top:14px;width:500px}
.row{display:flex;gap:8px;margin-bottom:22px}
.field{flex:1;height:22px;border:1px solid var(--line);background:var(--field);font-size:7px;color:var(--muted);display:flex;align-items:center;padding:0 6px;white-space:nowrap;overflow:hidden}
.btn-search{position:absolute;right:0;top:0;width:86px;height:99px;background:var(--blue);color:var(--white);
  display:flex;flex-direction:column;align-items:center;justify-content:center;gap:8px;font-size:8px;font-weight:700;letter-spacing:.5px}

.section-title{position:absolute;top:420px;width:758px;text-align:center;font-size:16px;font-weight:800;color:var(--navy);letter-spacing:.5px}
.section-sub{position:absolute;top:446px;width:758px;text-align:center;font-size:8px;color:var(--muted)}

.card{position:absolute;width:180px;height:240px;background:var(--white);box-shadow:0 2px 10px rgba(0,0,0,.1)}
.card-photo{position:relative;height:160px}
.price{position:absolute;right:0;bottom:0;background:var(--orange);color:var(--white);font-size:8px;font-weight:700;padding:5px 9px}
.tags{display:flex;gap:3px;margin:7px 0 0 8px}
.tag{font-size:5.5px;font-weight:700;color:var(--white);padding:2px 5px}
.tag-let{background:var(--red)}
.tag-new{background:var(--navy)}
.card-name{font-size:10px;font-weight:700;color:var(--navy);margin:5px 8px 0}
.card-addr{font-size:6px;color:var(--muted);margin:2px 8px 0}
.card-meta{display:flex;align-items:center;margin:9px 8px 0;font-size:6px;color:var(--muted)}
.card-meta .area{margin-right:auto}
.card-meta .feat{display:flex;align-items:center;gap:2px;margin-left:7px}

.btn-all{position:absolute;left:329px;top:1046px;width:101px;height:22px;background:var(--blue);color:var(--white);font-size:7px;font-weight:700;display:flex;align-items:center;justify-content:center;letter-spacing:.4px}

.cta-band{position:absolute;left:0;top:1113px;width:758px;height:87px;background:var(--navy);display:flex;align-items:center;padding:0 18px}
.cta-text{color:var(--white);font-size:17px;font-weight:400}
.cta-text span{color:var(--yellow)}
.btn-contact{margin-left:auto;margin-right:24px;background:var(--blue);color:var(--white);font-size:8px;font-weight:700;padding:8px 16px;letter-spacing:.5px}
</style>
</head>
<body>

<section class="hero" role="img" aria-label="Modern house photographed at dusk with warm lit windows">
  <div class="hero-glow"></div>
</section>

<header class="site-header">
  <div class="brand"><span class="brand-mark"></span><span class="brand-name">Maple Crest Property</span></div>
  <nav class="main-nav">
    <a>HOME</a><a>LETTINGS</a><a>PROPERTY MANAGEMENT</a><a>LANDLORDS</a><a>TENANTS</a><a>ABOUT</a><a>CONTACT</a>
  </nav>
  <span class="btn-submit">VALUATION</span>
</header>

<h1 class="hero-title">QUALITY HOMES <span>TO LET</span></h1>
<p class="hero-sub">Lettings and property management in Liverpool.</p>

<div class="search-tabs"><span class="tab-rent">RENT</span><span class="tab-manage">LANDLORDS</span></div>
<form class="search-panel">
  <div class="search-fields">
    <div class="row">
      <span class="field">Street, area or postcode</span>
      <span class="field">Location</span>
      <span class="field">Furnishing</span>
      <span class="field">All property types</span>
    </div>
    <div class="row">
      <span class="field">Bedrooms</span>
      <span class="field">Bathrooms</span>
      <span class="field">Available</span>
      <span class="field">Pets</span>
      <span class="field">Min rent</span>
      <span class="field">Max rent</span>
    </div>
  </div>
  <div class="btn-search">
    <svg width="26" height="26" viewBox="0 0 26 26"><circle cx="11" cy="11" r="8" fill="none" stroke="#fff" stroke-width="2.5"/><line x1="17" y1="17" x2="24" y2="24" stroke="#fff" stroke-width="3" stroke-linecap="round"/></svg>
    SEARCH
  </div>
</form>

<h2 class="section-title">WHAT'S NEW TO LET</h2>
<p class="section-sub">Check out some of our latest rental properties</p>

<article class="card" style="left:76px;top:493px">
  <div class="card-photo" role="img" aria-label="Bright white modern kitchen interior" style="background:linear-gradient(135deg,#eef0f2,#c9cdd2)"><span class="price">£950 pcm</span></div>
  <div class="tags"><span class="tag tag-let">TO LET</span><span class="tag tag-new">NEW</span></div>
  <h3 class="card-name">The Chalet Estate</h3>
  <p class="card-addr">27 Bath Road, Liverpool, United Kingdom</p>
  <div class="card-meta"><span class="area">Area: 1650 SqFt</span>
    <span class="feat"><svg width="8" height="6"><rect width="8" height="6" fill="#1e9be9"/></svg>3</span>
    <span class="feat"><svg width="8" height="6"><rect width="8" height="6" fill="#1e9be9"/></svg>2</span>
    <span class="feat"><svg width="8" height="6"><rect width="8" height="6" fill="#1e9be9"/></svg>Yes</span></div>
</article>

<article class="card" style="left:289px;top:493px">
  <div class="card-photo" role="img" aria-label="Open plan apartment living room with green accents" style="background:linear-gradient(135deg,#e6e8e2,#b9c0b0)"><span class="price">£795 pcm</span></div>
  <div class="tags"><span class="tag tag-let">TO LET</span><span class="tag tag-new">NEW</span></div>
  <h3 class="card-name">Morden Apartment</h3>
  <p class="card-addr">14 Park Lane, Liverpool, United Kingdom</p>
  <div class="card-meta"><span class="area">Area: 1420 SqFt</span>
    <span class="feat"><svg width="8" height="6"><rect width="8" height="6" fill="#1e9be9"/></svg>2</span>
    <span class="feat"><svg width="8" height="6"><rect width="8" height="6" fill="#1e9be9"/></svg>1</span>
    <span class="feat"><svg width="8" height="6"><rect width="8" height="6" fill="#1e9be9"/></svg>Yes</span></div>
</article>

<article class="card" style="left:502px;top:493px">
  <div class="card-photo" role="img" aria-label="White duplex lounge with large windows" style="background:linear-gradient(135deg,#f3f3f1,#cfcac2)"><span class="price">£1,150 pcm</span></div>
  <div class="tags"><span class="tag tag-let">TO LET</span><span class="tag tag-new">NEW</span></div>
  <h3 class="card-name">Luxurious Duplex</h3>
  <p class="card-addr">9 Mill Street, Liverpool, United Kingdom</p>
  <div class="card-meta"><span class="area">Area: 1890 SqFt</span>
    <span class="feat"><svg width="8" height="6"><rect width="8" height="6" fill="#1e9be9"/></svg>4</span>
    <span class="feat"><svg width="8" height="6"><rect width="8" height="6" fill="#1e9be9"/></svg>2</span>
    <span class="feat"><svg width="8" height="6"><rect width="8" height="6" fill="#1e9be9"/></svg>Yes</span></div>
</article>

<article class="card" style="left:76px;top:754px">
  <div class="card-photo" role="img" aria-label="Modern white kitchen with dining area" style="background:linear-gradient(135deg,#efeeea,#c7c3ba)"><span class="price">£875 pcm</span></div>
  <div class="tags"><span class="tag tag-let">TO LET</span><span class="tag tag-new">NEW</span></div>
  <h3 class="card-name">Westbourne House</h3>
  <p class="card-addr">5 Grove Road, Liverpool, United Kingdom</p>
  <div class="card-meta"><span class="area">Area: 1575 SqFt</span>
    <span class="feat"><svg width="8" height="6"><rect width="8" height="6" fill="#1e9be9"/></svg>3</span>
    <span class="feat"><svg width="8" height="6"><rect width="8" height="6" fill="#1e9be9"/></svg>2</span>
    <span class="feat"><svg width="8" height="6"><rect width="8" height="6" fill="#1e9be9"/></svg>Yes</span></div>
</article>

<article class="card" style="left:289px;top:754px">
  <div class="card-photo" role="img" aria-label="Bright living room with sofa and garden view" style="background:linear-gradient(135deg,#ecefe9,#b8c2b4)"><span class="price">£925 pcm</span></div>
  <div class="tags"><span class="tag tag-let">TO LET</span><span class="tag tag-new">NEW</span></div>
  <h3 class="card-name">Shamrock Place Garden</h3>
  <p class="card-addr">31 Elm Avenue, Liverpool, United Kingdom</p>
  <div class="card-meta"><span class="area">Area: 1720 SqFt</span>
    <span class="feat"><svg width="8" height="6"><rect width="8" height="6" fill="#1e9be9"/></svg>3</span>
    <span class="feat"><svg width="8" height="6"><rect width="8" height="6" fill="#1e9be9"/></svg>2</span>
    <span class="feat"><svg width="8" height="6"><rect width="8" height="6" fill="#1e9be9"/></svg>Yes</span></div>
</article>

<article class="card" style="left:502px;top:754px">
  <div class="card-photo" role="img" aria-label="Airy white sitting room with soft furnishings" style="background:linear-gradient(135deg,#f2f1ee,#cdc8c0)"><span class="price">£1,050 pcm</span></div>
  <div class="tags"><span class="tag tag-let">TO LET</span><span class="tag tag-new">NEW</span></div>
  <h3 class="card-name">Valmark Orchard</h3>
  <p class="card-addr">18 Oak Close, Liverpool, United Kingdom</p>
  <div class="card-meta"><span class="area">Area: 1810 SqFt</span>
    <span class="feat"><svg width="8" height="6"><rect width="8" height="6" fill="#1e9be9"/></svg>4</span>
    <span class="feat"><svg width="8" height="6"><rect width="8" height="6" fill="#1e9be9"/></svg>3</span>
    <span class="feat"><svg width="8" height="6"><rect width="8" height="6" fill="#1e9be9"/></svg>Yes</span></div>
</article>

<span class="btn-all">VIEW ALL LETTINGS</span>

<footer class="cta-band">
  <p class="cta-text">Are you a landlord? Get a free rental valuation <span>for your property</span></p>
  <span class="btn-contact">CONTACT US</span>
</footer>

</body>
</html>
```